Larkspur Ridge Management - Business Cards

I need business cards. My current logo was designed by a designer at this site and I very much like and am happy with the results. I would like a business card that is trendy, unique, current yet professional. I deal with high net worth clients daily

Target Market(s)

Out of state investors looking to get into the rental market in Ohio

Industry/Entity Type

Property Management, Consulting

Contact Information for Business Card

Name, Title (Chief Financial Officer) office phone number (555) 817-3094 website address larkridgemgmt.example

Font styles to use
Sans Serif

Colors
0054AA
0677BA
7BADD7
CADEEF
E8F1F8
0094D4
00A9DD
6FCCEA
C7EBF8
E9F6FB
00AB8E
00BBA5
67D7C9
C6EFE9
E9F9F6

```html
<!DOCTYPE html>
<html lang="en">
<head>
<meta charset="utf-8">
<title>Larkspur Ridge Management – Business Card</title>
<link rel="stylesheet" href="https://fonts.googleapis.com/css2?family=Montserrat:wght@600;700&family=Nunito+Sans:wght@400;600&display=swap">
<style>
  :root {
    --blue-deep: #0054AA;
    --blue-mid: #0677BA;
    --blue-soft: #7BADD7;
    --blue-mist: #CADEEF;
    --sky: #0094D4;
    --sky-bright: #00A9DD;
    --sky-soft: #6FCCEA;
    --teal: #00AB8E;
    --teal-bright: #00BBA5;
    --teal-soft: #67D7C9;
    --white: #ffffff;
    --paper: #E8F1F8;
  }
  * { box-sizing: border-box; margin: 0; padding: 0; }
  html, body {
    width: 1200px; height: 728px; overflow: hidden;
    background: var(--paper);
  }
  .card {
    position: absolute; left: 12px; width: 1176px; height: 346px;
    background: linear-gradient(120deg, #00468f 0%, var(--blue-deep) 55%, #005fb5 100%);
    overflow: hidden;
    box-shadow: 0 1px 3px rgba(0, 40, 90, 0.3);
  }
  .card--front { top: 11px; }
  .card--back { top: 367px; }

  .backdrop { position: absolute; top: 0; bottom: 0; }
  .backdrop--left {
    left: 0; width: 420px;
    background: linear-gradient(100deg, rgba(123,173,215,0.18), rgba(123,173,215,0) 85%);
  }
  .backdrop--right {
    right: 0; width: 440px;
    background: linear-gradient(260deg, rgba(123,173,215,0.18), rgba(123,173,215,0) 85%);
  }

  .frame { position: absolute; inset: 0; width: 100%; height: 100%; }

  .brand-name {
    position: absolute;
    font-family: "Montserrat", sans-serif; font-weight: 700;
    color: var(--white); text-align: center; text-transform: uppercase;
    line-height: 1.1;
  }
  .card--front .brand-name {
    left: 0; right: 0; top: 124px;
    font-size: 44px; letter-spacing: 1px;
  }
  .card--back .brand-name {
    left: 36px; width: 320px; top: 140px;
    font-size: 28px; letter-spacing: 0.5px;
  }

  .person { position: absolute; left: 443px; top: 52px; }
  .person__name {
    font-family: "Montserrat", sans-serif; font-weight: 700;
    font-size: 44px; color: var(--white); letter-spacing: 1.5px;
    line-height: 1;
  }
  .person__title {
    margin-top: 16px;
    font-family: "Nunito Sans", sans-serif; font-weight: 600;
    font-size: 18px; color: var(--sky-soft); letter-spacing: 2.4px;
  }

  .contact { position: absolute; left: 443px; }
  .contact--phone { top: 178px; }
  .contact--web { top: 228px; }
  .contact__icon {
    position: absolute; left: 0; top: 0; width: 38px; height: 38px;
  }
  .contact__bar {
    position: absolute; left: 60px; top: 9px; width: 2px; height: 20px;
    background: var(--sky-soft);
  }
  .contact__text {
    position: absolute; left: 95px; top: 3px; white-space: nowrap;
    font-family: "Nunito Sans", sans-serif; font-weight: 400;
    font-size: 22px; color: var(--white); letter-spacing: 0.5px;
  }
</style>
</head>
<body>

<section class="card card--front">
  <div class="backdrop backdrop--left" role="img" aria-label="Faint architectural line drawing of a modern building"></div>
  <div class="backdrop backdrop--right" role="img" aria-label="Faint architectural line drawing of a modern building"></div>
  <svg class="frame" viewBox="0 0 1176 346" aria-hidden="true">
    <polyline points="399,22 22,22 22,317" fill="none" stroke="var(--teal-bright)" stroke-width="2"/>
    <polyline points="1153,276 1153,323 776,323" fill="none" stroke="var(--teal-bright)" stroke-width="2"/>
  </svg>
  <p class="brand-name">Larkspur Ridge<br>Management</p>
</section>

<section class="card card--back">
  <div class="backdrop backdrop--left" role="img" aria-label="Faint architectural line drawing of a building"></div>
  <div class="backdrop backdrop--right" role="img" aria-label="Faint architectural line drawing of a modern house"></div>
  <svg class="frame" viewBox="0 0 1176 346" aria-hidden="true">
    <polygon points="0,0 286,0 331,54 419,164 271,346 0,346" fill="#00407f" opacity="0.8"/>
    <polygon points="286,0 377,0 331,54" fill="var(--teal)"/>
    <polyline points="377,0 331,54" fill="none" stroke="var(--sky-soft)" stroke-width="2"/>
    <polyline points="331,54 419,164 271,346" fill="none" stroke="var(--sky-soft)" stroke-width="2"/>
    <line x1="443" y1="149" x2="893" y2="149" stroke="var(--sky-soft)" stroke-width="1.5"/>
    <rect x="599" y="147.5" width="39" height="3.5" fill="var(--teal-bright)"/>
    <line x1="443" y1="301" x2="854" y2="301" stroke="var(--sky-soft)" stroke-width="1.5"/>
  </svg>

  <p class="brand-name">Larkspur Ridge<br>Management</p>

  <div class="person">
    <h1 class="person__name">MARCUS DELANEY</h1>
    <p class="person__title">CHIEF FINANCIAL OFFICER</p>
  </div>

  <div class="contact contact--phone">
    <svg class="contact__icon" viewBox="0 0 38 38" aria-hidden="true">
      <circle cx="19" cy="19" r="18" fill="var(--teal)" stroke="var(--teal-soft)" stroke-width="1"/>
      <path d="M13.5 11.5c.8-.8 1.8-.8 2.4 0l1.6 2.2c.5.7.4 1.5-.2 2.1l-1 1c.8 1.8 2.2 3.3 4 4.2l1-1c.6-.6 1.5-.7 2.1-.2l2.2 1.6c.8.6.8 1.6 0 2.4l-1.2 1.2c-1 1-2.6 1.2-4 .6-3.6-1.6-6.5-4.4-8.1-8.1-.6-1.4-.4-3 .6-4z" fill="var(--white)"/>
    </svg>
    <span class="contact__bar"></span>
    <span class="contact__text">(555) 817-3094</span>
  </div>

  <div class="contact contact--web">
    <svg class="contact__icon" viewBox="0 0 38 38" aria-hidden="true">
      <circle cx="19" cy="19" r="18" fill="var(--teal)" stroke="var(--teal-soft)" stroke-width="1"/>
      <g fill="none" stroke="var(--white)" stroke-width="1.4">
        <circle cx="19" cy="19" r="9"/>
        <ellipse cx="19" cy="19" rx="4" ry="9"/>
        <line x1="10" y1="19" x2="28" y2="19"/>
        <path d="M11.5 14.5h15M11.5 23.5h15"/>
      </g>
    </svg>
    <span class="contact__bar"></span>
    <span class="contact__text">larkridgemgmt.example</span>
  </div>
</section>

</body>
</html>
```